Migration and redesign of existing website to WordPress using DIVI 3

I. TASK OBJECTIVE:
- Redesign our existing website www.harlowsteppodiatry.com.au with a fresh new look and migrate to new Wordpress site based on DIVI3 theme. The site will contain the same basic functionality as the existing site (with some small changes).

II. STYLE/ DESIGN ASPECT:
As an example of a site that I like the look of, see https://quillmarsh.com/. I like the use of shadows, and this would go well with the little animations you can do with Divi (e.g. when hovering over pics).

1. What I am looking for is a design which has lots of white space, is modern and friendly looking (but still not too cute or frivolous, as we are a medical practice)
2. DESIGN that is NOT TOO rectangular or blocky.
3. Please take into consideration our Users are Older market, so any icons or navigation features need to be very easy to understand and not too small.
4. Must be easy to navigate
5. We are are happy to go with a new colour scheme, and are working on some ideas for this, but happy to take suggestions.

III. SPECIFICATIONS:
1. 5+ Pages (should flow like the current site)
2. Using Wordpress Divi 3 theme.
3. I'd like every page to have a "book now" button and a contact form in a sidebar so that users can click the button or fill in the contact form without scrolling at all. EXCEPT ON THE HOME PAGE, where there should still be a book now button (maybe on the top right in the header of all pages?), and maybe a contact us button which scrolls down to the contact area at the bottom of the HOME page. I don't think a side bar is necessarily required on the home page, but if you think it makes sense from a design perspective please let me know.
4. AT THE BOTTOM OF THE PAGE, just above the FOOTER, I'd like a row of trust logos for various organisations that we are affiliated with. (A list of this company will be provided later but you could temporarily use placeholders)

Once we have a structure in place, we can migrate most of the content. Please let me know if I'm not being clear or you need further information.

Podiatry Customers and Referrors

Health Care

Coded - Design and coding required

5+ page

Designer to choose colors to be used in the design.

• Simple to navigate.
• Contact/booking details on most if not all pages - please see specification above
• Section for Trusted Affiliates above the footer
• Wordpress using Divi3 Theme
• Not too busy with the design. Plenty of white space or light background.
• Should not be complicated to navigate.
• TOO rectangular or blocky designs

```html
<!DOCTYPE html>
<html lang="en">
<head>
<meta charset="utf-8">
<title>Harlow Step Podiatry</title>
<link href="https://fonts.googleapis.com/css2?family=Montserrat:wght@500;600;700&family=Open+Sans:wght@400;600&display=swap" rel="stylesheet">
<style>
:root{
  --teal:#2a9d9b;
  --teal-dark:#1f8886;
  --teal-soft:#d6f0ee;
  --pink-soft:#fbe3e3;
  --ink:#1f2a2e;
  --body:#5d666a;
  --line:#e3e7e8;
  --white:#ffffff;
}
*{box-sizing:border-box;margin:0;padding:0}
html,body{width:1200px;height:4749px;overflow:hidden}
body{position:relative;background:var(--white);font-family:"Open Sans",Arial,sans-serif;color:var(--body);font-size:13px;line-height:1.55}
.abs{position:absolute}
h1,h2,h3{font-family:"Montserrat",Arial,sans-serif;color:var(--ink);font-weight:700}
.btn{position:absolute;display:inline-block;white-space:nowrap;background:var(--teal);color:var(--white);font-family:"Montserrat",Arial,sans-serif;font-weight:600;font-size:13px;padding:0 22px;height:36px;line-height:36px;border-radius:3px;box-shadow:0 6px 14px rgba(31,136,134,.25)}
.flow .btn{position:static}
.section-title{position:absolute;left:0;width:1200px;text-align:center;font-size:30px}
.placeholder{position:absolute}
.blobs{position:absolute;left:0;top:0}

/* header */
.logo{left:196px;top:26px;display:flex;align-items:center;gap:10px}
.logo-dot{width:38px;height:38px;border-radius:50%;background:var(--teal)}
.logo-name{font-family:"Montserrat",Arial,sans-serif;font-weight:600;font-size:17px;color:var(--teal);white-space:nowrap}
.social{right:200px;top:18px;display:flex;gap:12px;align-items:center}
.social span{width:14px;height:14px;border-radius:50%;background:var(--teal-dark);display:block}
.social .search{width:26px;height:26px;border-radius:3px;background:var(--teal);display:flex;align-items:center;justify-content:center}
.phone{right:200px;top:62px;font-family:"Montserrat",Arial,sans-serif;font-size:20px;font-weight:500;color:var(--teal-dark);display:flex;align-items:center;gap:8px;white-space:nowrap}
.nav{left:168px;top:118px;width:864px;height:28px;display:flex;align-items:center;gap:20px;font-family:"Montserrat",Arial,sans-serif;font-size:12px;font-weight:600;color:var(--ink);white-space:nowrap}
.nav span{white-space:nowrap}
.nav .active{background:var(--teal);color:var(--white);padding:4px 16px;border-radius:3px}
.nav .book{margin-left:auto;background:var(--teal-dark);color:var(--white);padding:5px 20px;border-radius:3px}

/* hero */
.hero-title{left:168px;top:262px;width:460px;font-size:31px;line-height:1.2}
.hero-text{left:168px;top:352px;width:420px;font-size:12px}

/* practice areas */
.practice-card{left:168px;top:790px;width:864px;height:458px;background:var(--white);box-shadow:0 14px 40px rgba(0,0,0,.12);border-radius:4px}
.tabs{left:168px;top:790px;width:222px}
.tabs li{list-style:none;font-family:"Montserrat",Arial,sans-serif;font-weight:600;font-size:14px;color:var(--ink);padding:16px 40px;height:52px;white-space:nowrap}
.tabs li.on{color:var(--teal);background:var(--white);box-shadow:-6px 6px 16px rgba(0,0,0,.08)}
.tab-body{left:412px;top:836px;width:306px;font-size:12px;text-align:justify}
.conditions{left:732px;top:836px;width:290px}
.conditions li{list-style:none;font-size:11.5px;color:var(--teal);border-bottom:1px solid var(--line);padding:4px 0 5px}

/* story blocks */
.flow{position:absolute;display:flex;flex-direction:column;align-items:flex-start;gap:18px}
.block-title{font-size:27px;line-height:1.25}
.block-text{font-size:12px;text-align:justify}
.block-text p+p{margin-top:14px}

/* team */
.team{top:2572px;left:168px;width:864px;height:260px}
.member{position:absolute;top:0;width:190px;text-align:center}
.member .photo{width:150px;height:150px;border-radius:50%;margin:16px auto 0;background:radial-gradient(circle at 50% 40%,#f3d7c7,#c9a892)}
.member h3{font-size:15px;margin-top:18px;white-space:nowrap}
.member p{font-size:12px}
.member.featured{background:var(--white);box-shadow:0 16px 36px rgba(0,0,0,.14);height:256px;top:-8px}
.member .more{font-size:11px;color:#9aa3a6;margin-top:8px}
.arrow{position:absolute;font-size:20px;color:#9aa3a6;font-family:"Montserrat",Arial,sans-serif}

/* cases */
.case{position:absolute;top:3118px;width:270px;height:160px;display:flex;align-items:center;justify-content:center;font-family:"Montserrat",Arial,sans-serif;font-weight:700;font-size:15px;color:var(--ink)}
.case.photo{background:linear-gradient(135deg,#efdcd0,#dcc2b3)}
.case.featured{background:var(--white);box-shadow:0 16px 36px rgba(0,0,0,.14);flex-direction:column;color:var(--teal)}
.case.featured small{font-family:"Open Sans",Arial,sans-serif;font-weight:400;font-size:11px;color:#9aa3a6;margin-top:60px}

/* affiliations */
.affiliates{left:190px;top:3975px;width:820px;display:flex;justify-content:space-between;align-items:center}
.affiliates span{display:block;width:150px;height:56px;background:#e4e7e8;border-radius:28px}

/* contact */
.field{position:absolute;height:38px;border:1px solid var(--line);background:var(--white);box-shadow:0 4px 10px rgba(0,0,0,.05);font-size:11px;color:#9aa3a6;padding:10px 10px}
.footer{left:0;top:4660px;width:1200px;height:89px;background:var(--teal-dark);color:var(--white);font-size:11px}
.footer .copy{position:absolute;left:168px;top:38px}
.footer .dots{position:absolute;right:168px;top:38px;display:flex;gap:14px}
.footer .dots span{width:12px;height:12px;border-radius:50%;background:var(--white);display:block}
</style>
</head>
<body>

<svg class="blobs" width="1200" height="4749" viewBox="0 0 1200 4749" aria-hidden="true">
  <path d="M1200 160 C1040 190 960 320 990 450 C1030 600 1180 620 1200 610 Z" fill="var(--teal-soft)" opacity=".6"/>
  <path d="M0 800 C150 600 420 560 620 640 C820 720 1000 600 1200 560 L1200 1330 C1000 1420 760 1360 560 1400 C320 1440 120 1380 0 1410 Z" fill="var(--teal-soft)" opacity=".7"/>
  <circle cx="940" cy="1700" r="210" fill="var(--pink-soft)"/>
  <circle cx="330" cy="2160" r="220" fill="var(--teal-soft)"/>
  <path d="M0 2700 C200 2560 420 2700 640 2640 C860 2580 1000 2400 1200 2430 L1200 2960 C900 2920 600 3010 300 2960 C150 2935 60 2960 0 2980 Z" fill="var(--pink-soft)" opacity=".9"/>
  <path d="M0 3220 C250 3150 500 3260 760 3230 C980 3200 1100 3160 1200 3180 L1200 3320 C900 3340 500 3300 0 3330 Z" fill="var(--teal-soft)" opacity=".7"/>
  <circle cx="840" cy="3610" r="170" fill="var(--teal-soft)"/>
  <path d="M0 4240 C300 4120 600 4240 900 4180 C1050 4150 1150 4130 1200 4140 L1200 4660 L0 4660 Z" fill="var(--teal-soft)" opacity=".55"/>
</svg>

<!-- header -->
<div class="abs logo"><span class="logo-dot"></span><span class="logo-name">Harlow Step Podiatry</span></div>
<div class="abs social"><span></span><span></span><span></span><span></span>
  <div class="search"><svg width="14" height="14" viewBox="0 0 14 14"><circle cx="6" cy="6" r="4.2" fill="none" stroke="#fff" stroke-width="1.8"/><line x1="9" y1="9" x2="13" y2="13" stroke="#fff" stroke-width="1.8"/></svg></div>
</div>
<div class="abs phone"><svg width="16" height="16" viewBox="0 0 16 16"><path d="M3 1.5l3 3-1.6 1.8c.8 1.8 2.3 3.3 4.1 4.1L10.3 9l3.2 3-1.8 2.2C6.4 14 1.9 9.6 1.6 4.2Z" fill="none" stroke="var(--teal-dark)" stroke-width="1.3"/></svg>(08) 5550 2147</div>
<nav class="abs nav">
  <span class="active">Home</span><span>Common Problems ▾</span><span>Services ▾</span><span>About Us ▾</span><span>Case Histories</span><span>Helpful Info ▾</span><span>Blog</span><span>Contact</span><span class="book">Book Now</span>
</nav>

<!-- hero -->
<h1 class="abs hero-title">We offer solutions to common foot problems</h1>
<p class="abs hero-text">Whether you want to clear a recurring condition, ease ongoing back strain or restore lost function, our podiatrists can advise you on the best way to get you moving again.</p>
<span class="btn" style="left:168px;top:428px">End Your Suffering Today!</span>
<div class="placeholder" role="img" aria-label="Photo of a pair of bare feet resting together" style="left:600px;top:215px;width:440px;height:330px;border-radius:50% 40% 45% 55%;background:radial-gradient(ellipse at 55% 50%,#f6d9c6,#e9bfa3 70%,rgba(255,255,255,0) 72%)"></div>
<div class="abs" style="left:995px;top:525px;width:56px;height:56px;border-radius:50%;background:var(--teal-soft)"></div>

<!-- practice areas -->
<h2 class="section-title" style="top:715px">Practice Areas</h2>
<div class="abs practice-card"></div>
<ul class="abs tabs">
  <li class="on">Common Problems</li><li>Foot &amp; Ankle Surgery</li><li>Sport &amp; Dance</li><li>All Our Services</li>
</ul>
<p class="abs tab-body">Foot and ankle pain can be distressing and uncomfortable, and some conditions may require surgery. If your foot or ankle problem needs surgical care, you want experienced, skilled hands. Our clinic offers a complete range of surgical treatments, from simple procedures to correct ingrown toenails to more complex reconstructive surgery for bunions, neuromas and problems with the middle and back of the foot. Our team of podiatrists is committed to improving our patients' quality of life through thorough, supportive foot and ankle care. For more information call our front desk today on (08) 5550 2147.</p>
<ul class="abs conditions">
  <li>Achilles Tendon Injuries</li><li>Ankle Sprains</li><li>Bunions</li><li>Corns and Calluses</li><li>Heel and Arch Pain</li><li>High Arch Foot (Pes Cavus)</li><li>Ingrown Toenails</li><li>Fungal Nails</li><li>Flatfoot</li><li>Skin and Nail Care</li><li>Stiff Big Toe (Hallux Rigidus)</li>
</ul>
<span class="btn" style="left:662px;top:1166px">View All</span>

<!-- block one -->
<div class="flow" style="left:168px;top:1508px;width:440px">
  <h2 class="block-title">Let Our Ashbury Vale Podiatrists Relieve Your Foot and Ankle Pain</h2>
  <div class="block-text">
    <p>Whether you are an office worker, pensioner or professional athlete, nearly all people will experience problems in their feet and ankles at some point in their lives. Often a problem in the foot can affect the whole body, causing pain elsewhere.</p>
    <p>It doesn't take long before a foot injury causes wide-ranging consequences, including lost mobility and strain on your finances. Many patients attempt to cure these conditions alone, but they often suffer the frustration of the symptoms returning.</p>
  </div>
</div>
<div class="placeholder" role="img" aria-label="Photo of a woman's smooth legs and feet" style="left:620px;top:1495px;width:420px;height:350px;border-radius:46% 54% 40% 60%;background:linear-gradient(160deg,#f4d6c3,#e5b99d)"></div>
<div class="abs" style="left:940px;top:1620px;width:66px;height:66px;border-radius:50%;background:var(--white);box-shadow:0 8px 20px rgba(0,0,0,.12)"></div>

<!-- block two -->
<div class="placeholder" role="img" aria-label="Photo of a runner mid-stride with strapped knee" style="left:185px;top:1975px;width:410px;height:420px;border-radius:40% 60% 55% 45%;background:linear-gradient(135deg,#efd2bf,#c99a7f)"></div>
<div class="abs" style="left:255px;top:2090px;width:80px;height:80px;border-radius:50%;background:var(--white);box-shadow:0 8px 20px rgba(0,0,0,.12)"></div>
<div class="flow" style="left:611px;top:1970px;width:420px">
  <h2 class="block-title">A Proven Track Record of Correcting Foot Pain in Perth Patients</h2>
  <div class="block-text">
    <p>At our clinic we know that there are a variety of causes of foot and ankle pain, and each must be addressed to solve your problem for good. We examine your foot, posture and gait to identify any biomechanical issues that could be causing your pain, and treat the underlying cause to restore mobility.</p>
    <p>Our practice has provided comprehensive podiatry care to all age groups across the region for many years. Since opening we have grown our team and services, and we continue to invest in modern equipment for our patients.</p>
  </div>
  <span class="btn">Read More</span>
</div>

<!-- team -->
<h2 class="section-title" style="top:2488px">Meet Our Team</h2>
<span class="arrow" style="left:150px;top:2690px">‹</span>
<span class="arrow" style="left:1040px;top:2690px">›</span>
<div class="abs team">
  <div class="member" style="left:0"><div class="photo" role="img" aria-label="Portrait of podiatric surgeon"></div><h3>Nora Whitfield</h3><p>Podiatric Surgeon</p></div>
  <div class="member" style="left:220px"><div class="photo" role="img" aria-label="Portrait of podiatrist"></div><h3>Callum Reyes</h3><p>Podiatrist</p></div>
  <div class="member featured" style="left:445px"><div class="photo" role="img" aria-label="Portrait of podiatrist"></div><h3 style="color:var(--teal)">Priya Landry</h3><p>Podiatrist</p><p class="more">Learn More →</p></div>
  <div class="member" style="left:665px"><div class="photo" role="img" aria-label="Portrait of podiatrist"></div><h3>Elise Dunmore</h3><p>Podiatrist</p></div>
</div>
<span class="btn" style="left:530px;top:2874px">View All Members</span>

<!-- case histories -->
<h2 class="section-title" style="top:3036px">Case Histories</h2>
<span class="arrow" style="left:150px;top:3182px">‹</span>
<span class="arrow" style="left:1040px;top:3182px">›</span>
<div class="case photo" style="left:168px" role="img" aria-label="Photo of a foot being examined">Plantar fascia Case</div>
<div class="case featured" style="left:465px">Bunion Case<small>Learn More →</small></div>
<div class="case photo" style="left:760px" role="img" aria-label="Photo of a bandaged ankle">Trauma Case</div>
<span class="btn" style="left:517px;top:3330px">View All Case Histories</span>

<!-- book -->
<div class="flow" style="left:168px;top:3530px;width:540px">
  <h2 class="block-title" style="font-size:26px">Free Foot Surgery Book by Podiatric Surgeon, Dr Nora Whitfield</h2>
  <p class="block-text" style="width:440px;text-align:left">This book was created to demonstrate examples of common foot conditions that can be surgically corrected by our Podiatric Surgeon, Dr Nora Whitfield.</p>
  <span class="btn">View Details</span>
</div>
<div class="placeholder" role="img" aria-label="Cover of a podiatric surgery book showing surgeons in theatre" style="left:722px;top:3450px;width:220px;height:320px;background:linear-gradient(180deg,#2b5f9e 0%,#2b5f9e 35%,#7aa7c9 36%,#9fc3d8 100%);box-shadow:12px 14px 26px rgba(0,0,0,.22)"></div>

<!-- affiliations -->
<h2 class="section-title" style="top:3870px">Affiliations</h2>
<div class="abs affiliates"><span></span><span></span><span></span><span></span></div>

<!-- contact -->
<h2 class="section-title" style="top:4222px">Contact Us</h2>
<div class="field" style="left:168px;top:4296px;width:272px">Name*</div>
<div class="field" style="left:464px;top:4296px;width:272px">Phone*</div>
<div class="field" style="left:760px;top:4296px;width:272px">Email*</div>
<div class="field" style="left:168px;top:4356px;width:864px;height:190px">Full enquiry</div>
<span class="btn" style="left:934px;top:4562px;height:32px;line-height:32px">Submit</span>

<footer class="abs footer">
  <span class="copy">©2017 Harlow Step Podiatry. All Rights Reserved. Privacy Policy</span>
  <div class="dots"><span></span><span></span><span></span><span></span></div>
</footer>

</body>
</html>
```